Amazon Fly/Cruise Expedition Cruise Package.

Task Description
I am wanting to create a double sided A4 colour flyer (Finished size: 297 x 210mm) for a Fly/Cruise package from Australia to the Amazon.
The idea is that I would like the art work or design work done for the flyer that I can then send to a printer to do the printing of these flyers.

My business is a retail cruise travel agent that specializes in selling all-inclusive packages on luxury expedition ships and in this case I intend to promote this cruise to people that are interested in wildlife and also bird watching.

This link will show you the full brochure from the Tour Operator that we will be using to give you more information on them and the cruise we are travelling on.
https://www.orvatrips.com/expedition/amazon-voyage#overview
This is an American company and basically I am giving you there brochure to give you more information.

I do all the costing's from Australia and ask you ignore the costing's etc. in their brochure, it will however give you more information to work with.

I will also attach my logo so this can be included and a copy of the draft itinerary that I see as being the highlights however I am aware that we are limited on space and we need to get the key issues across and also as the trip is being marketed to bird watchers and wildlife enthusiasts then some good pictures of both the boat and a few good birds ones and let’s say a bird called a ????? and maybe a monkey.

We also need to show the costing's and what's included in the package.

And of course a call to action
All bookings and enquiries call Derek

1-300-419-873
WaveHarbor Pty Ltd
derek@waveharbor.com.au
PO Box 817
Kelton NSW 2031
Australia.

Target Market(s)

Travellers that are interested in Birds/Animals and Expedition cruising.

Colors

Designer to choose colors to be used in the design.

Requirements
Must have
• Easy to read
• Colour full
• 2 birds pics
• 1 photo of the boat
• waveharbor logo
Nice to have
• a crisp clean look and a professional appearance

```html
<!DOCTYPE html>
<html lang="en">
<head>
<meta charset="utf-8">
<title>Explore the Peruvian Amazon – Flyer</title>
<link rel="stylesheet" href="https://fonts.googleapis.com/css2?family=Lexend:wght@300;400;500&family=Open+Sans:wght@400;600&display=swap">
<style>
  :root{
    --green:#2bb673;
    --black:#0b0b0b;
    --ink:#2a2a2a;
    --paper:#ffffff;
    --stage:#b9babc;
    --footer:#f2f2f2;
    --rule:#bdbdbd;
    --navy:#23409a;
  }
  *{box-sizing:border-box;margin:0;padding:0}
  html,body{width:1200px;height:1200px;overflow:hidden;background:var(--stage)}
  body{position:relative;font-family:"Open Sans",sans-serif;color:var(--ink)}
  .page{position:absolute;background:var(--paper);width:533px;height:752px;overflow:hidden}
  .front{left:58px;top:160px}
  .back{left:609px;top:294px}
  .photo{position:absolute}
  .heading{font-family:"Lexend",sans-serif}

  /* front */
  .photo-expedition{left:0;top:14px;width:399px;height:211px;background:linear-gradient(180deg,#3f6a3a 0%,#5d8f3e 45%,#7fb04a 100%)}
  .photo-bird{left:408px;top:15px;width:125px;height:102px;background:linear-gradient(135deg,#5b8d3a,#2e7fb8 55%,#4a7a2c)}
  .photo-ship{left:408px;top:131px;width:125px;height:94px;background:linear-gradient(180deg,#6fa6d6 0%,#a9c9e4 50%,#8a6f55 75%,#5a6e7a 100%)}
  .tagline{position:absolute;left:0;top:234px;width:399px;height:41px;background:var(--black);color:#fff;font-family:"Lexend",sans-serif;font-size:16px;line-height:41px;padding-left:20px;letter-spacing:.2px}
  .squares{position:absolute;left:409px;top:234px;display:grid;grid-template-columns:repeat(7,11px);grid-auto-rows:11px;gap:8px}
  .squares span{background:var(--green)}
  .title-1{position:absolute;left:8px;top:290px;font-size:38px;font-weight:400;color:var(--black);letter-spacing:.5px}
  .title-2{position:absolute;left:8px;top:338px;font-size:36.5px;font-weight:500;color:var(--green);white-space:nowrap;letter-spacing:-.2px}
  .title-2 small{font-size:7px;color:var(--black);font-weight:400;margin-left:5px;letter-spacing:0}
  .highlights{position:absolute;left:20px;top:393px;width:430px;list-style:none}
  .highlights li{position:relative;padding-left:24px;font-size:8.2px;line-height:14.4px;margin-bottom:4px}
  .highlights li:nth-child(2){margin-bottom:13px}
  .highlights li::before{content:"";position:absolute;left:0;top:3px;width:10px;height:9px;background:var(--green);box-shadow:1px 1px 2px rgba(0,0,0,.35)}
  .brand-bar{position:absolute;left:0;top:655px;width:533px;height:12px;background:linear-gradient(90deg,var(--navy),#1f8a9a 45%,var(--green))}
  .footer{position:absolute;left:0;top:667px;width:533px;height:85px;background:var(--footer)}
  .logo{position:absolute;left:24px;top:18px;display:flex;align-items:center;gap:5px;font-family:"Lexend",sans-serif;font-size:15px;font-weight:500;color:#555}
  .logo i{width:10px;height:10px;background:#777;display:block}
  .about{position:absolute;left:166px;top:9px;width:150px;font-size:7px;line-height:10px}
  .phone{position:absolute;left:333px;top:9px;display:flex;align-items:center;gap:5px;font-family:"Lexend",sans-serif;font-size:21px;color:var(--black)}
  .icon{width:22px;height:22px;border-radius:50%;background:var(--green);display:flex;align-items:center;justify-content:center}
  .contacts{position:absolute;left:29px;top:55px;width:490px;display:flex;justify-content:space-between;font-size:7px}
  .contacts span{display:flex;align-items:center;gap:5px}
  .contacts .icon{width:13px;height:13px}

  /* back */
  .header{position:absolute;left:0;top:13px;width:533px;height:38px;display:flex;font-family:"Lexend",sans-serif;color:#fff}
  .header .label{background:var(--black);width:166px;font-size:16.5px;line-height:38px;padding-left:11px}
  .header .call{flex:1;background:var(--green);font-size:16.5px;line-height:38px;padding-left:7px;white-space:nowrap}
  .header .call small{font-size:6.3px;margin-left:3px}
  .arrival{position:absolute;left:26px;top:80px;display:flex;align-items:center;gap:9px;font-size:6.5px}
  .arrival i{width:12px;height:11px;background:var(--green);box-shadow:1px 1px 2px rgba(0,0,0,.3);display:block}
  .days{position:absolute;left:0;width:533px;display:flex}
  .days .labels{width:73px;display:flex;flex-direction:column;font-family:"Lexend",sans-serif;color:var(--green);font-size:16px}
  .days .texts{flex:1;border-left:1px solid var(--rule);padding:0 4px 0 3px;font-size:6.5px;line-height:9.6px}
  .days.right{flex-direction:row-reverse}
  .days.right .texts{border-left:none;border-right:1px solid var(--rule);padding:0 3px 0 9px}
  .days.right .labels{width:68px;padding-left:10px}
  .texts p{margin-bottom:3px}
  .set-1{top:121px}
  .set-1 .labels{padding:6px 0 0 9px;gap:16px}
  .set-2{top:233px;border-top:1px solid var(--rule);padding-top:4px}
  .set-2 .labels{padding-top:10px;gap:20px}
  .set-3{top:394px}
  .set-3 .labels{padding:11px 0 0 14px;gap:16px}
  .set-4{top:510px;border-top:1px solid var(--rule);padding-top:3px}
  .set-4 .labels{padding-top:10px}
  .ship{position:absolute;left:0;top:605px;width:533px;height:133px;display:flex}
  .photo-ship-side{position:relative;width:124px;height:133px;background:linear-gradient(180deg,#6c9fcf 0%,#b3cfe6 45%,#6a5040 70%,#9b8066 100%)}
  .ship-info{flex:1;background:var(--green);color:#fff;padding:3px 10px 0 5px}
  .ship-info h2{font-family:"Lexend",sans-serif;font-weight:400;font-size:15px;color:var(--black);margin:0 0 10px 3px}
  .ship-info p{font-size:6.5px;line-height:9.7px;margin-bottom:10px}
</style>
</head>
<body>

<section class="page front">
  <div class="photo photo-expedition" role="img" aria-label="Photo of travellers on a small boat watching wildlife among green river plants"></div>
  <div class="photo photo-bird" role="img" aria-label="Photo of a colourful blue tropical bird among leaves"></div>
  <div class="photo photo-ship" role="img" aria-label="Photo of the expedition riverboat"></div>

  <div class="tagline">10 DAYS OF BREATH TAKING EXPEDITION</div>
  <div class="squares">
    <span></span><span></span><span></span><span></span><span></span><span></span><span></span>
    <span></span><span></span><span></span><span></span><span></span><span></span><span></span>
    <span></span><span></span><span></span><span></span><span></span><span></span><span></span>
  </div>

  <h1 class="heading title-1">EXPLORE</h1>
  <div class="heading title-2">THE PERUVIAN AMAZON<small>RAINFOREST</small></div>

  <ul class="highlights">
    <li>Explore the Peruvian Amazon rainforest and its tributaries, experience wildlife as you voyage deep into the amazon river onboard the Esmeralda Star, a luxurious vessel that combines a blend of stylish design and modern comforts.</li>
    <li>Visit local communities and experience a range of cultural diversity, explore villages along the amazon river with a chance to learn about the lives of the people who live there, how they live, learn and grow.</li>
    <li>Go fishing in grand style, find gray river dolphins, try your hand at piranha fishing in Ubas lake and find other fishing experiences. Also find birds like The Hyacinth Macaw, Blue Fronted Amazon Scarlet Macaws, Spectacled Owl, Plum Throated Cotinga, Crimson Topaz, Oropendolas and the Amazon Kingfisher.</li>
    <li>Enjoy stargazing and storytelling with our guides while cruising slowly on the Amazon river, enjoy nighttime boat excursions for a chance to find caimans, common potos, frogs and other nocturnal wildlife.</li>
    <li>Experience multiple daily excursions to see wildlife, explore the Pacay-samiria reserve, home to 450 bird species, 102 species of mammals, over 130 species of reptiles and amphibians and countless plants. Find Giant River Otters, Toucans, Macaws, Black Caimans, Capybaras, Pink River Dolphins, Piranhas and Jaguars.</li>
  </ul>

  <div class="brand-bar"></div>
  <footer class="footer">
    <div class="logo"><i></i>WaveHarbor</div>
    <p class="about">WaveHarbor is a retail cruise travel agency that specializes in all-inclusive packages on luxury expedition ships &amp; travels</p>
    <div class="phone">
      <span class="icon"><svg width="12" height="12" viewBox="0 0 24 24"><path fill="#fff" d="M6.6 10.8a15 15 0 0 0 6.6 6.6l2.2-2.2c.3-.3.7-.4 1-.2 1.1.4 2.3.6 3.6.6.6 0 1 .4 1 1V20c0 .6-.4 1-1 1A17 17 0 0 1 3 4c0-.6.4-1 1-1h3.5c.6 0 1 .4 1 1 0 1.2.2 2.4.6 3.6.1.3 0 .7-.2 1z"/></svg></span>
      1-300-419-873
    </div>
    <div class="contacts">
      <span><span class="icon"><svg width="8" height="8" viewBox="0 0 24 24"><circle cx="12" cy="12" r="9" fill="none" stroke="#fff" stroke-width="3"/><path d="M3 12h18M12 3c3 3 3 15 0 18M12 3c-3 3-3 15 0 18" fill="none" stroke="#fff" stroke-width="2"/></svg></span>waveharbor.com.au</span>
      <span><span class="icon"><svg width="8" height="8" viewBox="0 0 24 24"><path fill="#fff" d="M12 2a7 7 0 0 0-7 7c0 5 7 13 7 13s7-8 7-13a7 7 0 0 0-7-7zm0 9.5A2.5 2.5 0 1 1 12 6.5a2.5 2.5 0 0 1 0 5z"/></svg></span>Kelton NSW 2031, Australia.</span>
      <span><span class="icon"><svg width="8" height="8" viewBox="0 0 24 24"><path fill="#fff" d="M3 5h18v14H3z"/><path d="M3 5l9 7 9-7" fill="none" stroke="#2bb673" stroke-width="2"/></svg></span>derek@waveharbor.com.au</span>
    </div>
  </footer>
</section>

<section class="page back">
  <header class="header">
    <div class="label">DAILY ITINERARY</div>
    <div class="call">CALL DEREK&nbsp; 1-300-419-873<small>FOR BOOKINGS &amp; ENQUIRIES</small></div>
  </header>

  <div class="arrival"><i></i>Fly from Australia to Lima Transfer from the airport to the Harborview Hotel Lima</div>

  <div class="days set-1">
    <div class="labels"><span>DAY 1</span><span>DAY 2</span><span>DAY 3</span></div>
    <div class="texts">
      <p>Tour the historic district of Lima. Visit the cathedral, where Francisco Pizarro is entombed, the Plaza de Armas, the monastery and vast catacombs of the Iglesia de San Francisco before visiting Casa Solana. Afterwards, we tour the ruins built by a Pre-Incan indigenous coastal civilization...</p>
      <p>Today we begin with a visit to the vibrant Indian Market where crafters display a wide variety of handmade items, jewelry, and art. We have lunch at a local restaurant and explore the surrounding shops before returning to the hotel to refresh before a late afternoon visit to the Andean Heritage Museum. We return to the hotel this evening and prepare for the next mornings' flight to Iquitos from Lima</p>
      <p>Fly over the Andes to Iquitos. Visit the Manatee Rescue Center, where biologists and volunteers care for endangered Amazon manatees that conservation authorities have rescued. Learn about efforts to help these endearing mammals. Board the elegant riverboat, Esmeralda Star, home for seven nights.</p>
    </div>
  </div>

  <div class="days right set-2">
    <div class="labels"><span>DAY 4</span><span>DAY 5</span><span>DAY 6</span></div>
    <div class="texts">
      <p>We awake this morning on the Amazon River, seeing some of the ever-changing panorama of jungle life as the Amazon River cruise ship continues upriver. Small villages dot the shoreline, and channels weaving through island mazes provide close-up views of a variety of birds.Later we take an excursion into the surrounding rainforest in search of giant water lilies and elusive wildlife such as monkeys and sloths.</p>
      <p>After a peaceful breakfast along the black-water Sapote Creek, we explore a small tributary of the Ucayali aboard excursion boats. Look for animals including primates, sloths and an enormous variety of birds. Our Amazon Voyage adventure continues upriver to the Pacaya-Samiria Reserve. We enjoy a nighttime boat excursion for a chance to find caimans, capybaras, common potoos, frogs and other nocturnal wildlife.</p>
      <p>Spend the day exploring this flooded realm, seeing wading birds such as herons, wattled jacanas and horned screamers. Venturing deep into the rainforest, tour an igapo (seasonally flooded forest), where plant life is very different from what we see along the main course of our Amazon cruise. A delicious lunch energizes us for afternoon excursions with our expert naturalists, where we may find scarlet macaws, hoatzins, black-collared hawks and red howler monkeys.</p>
    </div>
  </div>

  <div class="days set-3">
    <div class="labels"><span>DAY 7</span><span>DAY 8</span><span>DAY 9</span></div>
    <div class="texts">
      <p>After an early breakfast, we board excursion boats for access even further into the heart of these vast wetlands. As our Amazon Voyage adventure cruises the narrow waterways, we'll find birds such as canary-winged parakeets and spectacular blue-and-gold and scarlet macaws. Enjoy an al fresco lunch and time to relax before our afternoon excursion.</p>
      <p>Head back downriver, with a morning wildlife or other activity. Visit a village along the river, with the chance to learn about the lives of the "Ribereño" people who live there. Aboard the ship, learn to make traditional Peruvian dishes or enjoying an enriching lecture. After dark, go out in excursion boats to listen to the sounds of the rainforest and look for nocturnal wildlife.</p>
      <p>Wake up early for a morning birdwatching excursion along the Yarapa River. After breakfast, try your hand at piranha fishing in Ubos Lake. Piranha are very common in the slower-moving water. Once back aboard your luxury Amazon River cruise ship, we enjoy a farewell dinner.</p>
    </div>
  </div>

  <div class="days right set-4">
    <div class="labels"><span>DAY 10</span></div>
    <div class="texts">
      <p>On an early morning excursion to Mariposa Rescue Center, see two- and three-toed sloth, red uakari and even a jaguar which have been rescued. Upon arrival back in Lima late this afternoon, dayrooms are provided until time to connect with independent overnight flights home. we fly from Iquitos to Lima where we connect with our flight back to Australia and arrive back in Sydney on the 27th April or you may wish to extend your trip.</p>
    </div>
  </div>

  <div class="ship">
    <div class="photo-ship-side" role="img" aria-label="Photo of the expedition riverboat on the Amazon"></div>
    <div class="ship-info">
      <h2>The Esmeralda Star</h2>
      <p>Travel aboard the Esmeralda Star, a luxurious vessel we have chartered for your adventure, which blends stylish design and modern comforts. Classic touches include magnificent floor-to-ceiling windows and — for those on the Upper Deck — private balconies. A ship staff and crew of 25, including a cruise director and local naturalist guides, are joined by an Orva Expedition Leader , Martin and Derek to ensure an unprecedented level of service. All 19 spacious suites are air-conditioned and feature en-suite bathrooms, a desk and ample closet space.</p>
      <p>We will be travelling in the High Water season this will allow us to go deeper into the Amazon Basin and further into the forest on our excursion boats we can also go into smaller tributaries- we will I hope see more wildlife and Birds that shun the main course of the river.</p>
    </div>
  </div>
</section>

</body>
</html>
```